Market Research firm needs updated business cards with new logo

We need the logo to be included somewhere on the card (attached). We would also like the phrases "Independent, Objective, Comprehensive" and "Research You Can Trust" somewhere on the card. Front or back. Our colors are hex codes 6075a7, e48d25 and 5a5b5b. Though you are certainly not limited to those shades, whatever you produce should coordinate with them. I have also attached our favicon. Feel free to use it in your design, but please do not use it to replace the full logo.

Contact Information for Business Card

see project description

Other font styles liked:
• Open Sans

Requirements
Must have
• the logo
• We use Open Sans font

```html
<!DOCTYPE html>
<html lang="en">
<head>
<meta charset="utf-8">
<title>Veranta Research – Business Card</title>
<link rel="stylesheet" href="https://fonts.googleapis.com/css2?family=Open+Sans:wght@400;600;700&display=swap">
<style>
  :root {
    --stage: #d9dadc;
    --slate: #6b7a8b;
    --orange: #f5821f;
    --ink: #5f6b78;
    --paper: #ffffff;
  }
  * { margin: 0; padding: 0; box-sizing: border-box; }
  html, body {
    width: 1200px; height: 930px; overflow: hidden;
    background: var(--stage);
    font-family: "Open Sans", sans-serif;
  }
  .card {
    position: absolute;
    width: 560px; height: 320px;
    border-radius: 24px;
    overflow: hidden;
    box-shadow: 0 6px 18px rgba(0,0,0,0.18);
  }
  .card--back {
    left: 80px; top: 80px;
    background: var(--slate);
    color: var(--paper);
  }
  .card--front {
    left: 560px; top: 530px;
    background: var(--paper);
  }
  .wordmark {
    display: flex; align-items: center; gap: 10px;
    font-weight: 400; letter-spacing: -0.5px;
    white-space: nowrap;
  }
  .wordmark__dot {
    width: 16px; height: 16px; border-radius: 50%;
    background: var(--orange); flex: none;
  }
  .card--back .wordmark {
    position: absolute; left: 0; right: 0; top: 118px;
    justify-content: center;
    font-size: 46px; color: var(--paper);
  }
  .card--back .wordmark__dot { width: 18px; height: 18px; }
  .tagline {
    position: absolute; left: 0; right: 0; bottom: 46px;
    text-align: center; font-size: 15px; line-height: 1.45;
    letter-spacing: 0.6px;
  }
  .card--front .wordmark {
    position: absolute; left: 34px; top: 140px;
    font-size: 26px; color: var(--ink);
  }
  .divider {
    position: absolute; left: 300px; top: 46px;
    width: 2px; height: 170px; background: var(--orange);
  }
  .contact {
    position: absolute; left: 320px; top: 40px;
    color: var(--ink); font-size: 13px; line-height: 1.55;
  }
  .contact__name {
    color: var(--orange); font-weight: 700; font-size: 20px;
    letter-spacing: 0.5px; text-transform: uppercase; line-height: 1.2;
  }
  .contact__role { font-size: 14px; margin-bottom: 8px; }
  .contact__address { margin-bottom: 6px; }
  .contact__line { display: flex; align-items: center; gap: 8px; }
  .contact__line svg { width: 11px; height: 11px; flex: none; }
  .band { position: absolute; left: 0; bottom: 0; width: 560px; height: 24px; }
</style>
</head>
<body>

<section class="card card--back">
  <div class="wordmark"><span class="wordmark__dot"></span>Veranta Research</div>
  <p class="tagline">Independent - Objective - Comprehensive<br>Research You Can Trust</p>
</section>

<section class="card card--front">
  <div class="wordmark"><span class="wordmark__dot"></span>Veranta Research</div>
  <div class="divider"></div>
  <div class="contact">
    <p class="contact__name">Daniel Hart</p>
    <p class="contact__role">Director</p>
    <p class="contact__address">1276 Larkspur Lane<br>Fairhaven, VA 22900</p>
    <p class="contact__line">
      <svg viewBox="0 0 12 12"><path d="M2.5 1 L4.5 1 L5.2 3.5 L4 4.6 Q5 7 7.4 8 L8.5 6.8 L11 7.5 L11 9.5 Q10.5 11 9 11 Q1 10 1 3 Q1 1.5 2.5 1 Z" fill="#f5821f"/></svg>
      555 010-2468
    </p>
    <p class="contact__line">
      <svg viewBox="0 0 12 12"><rect x="1" y="2.5" width="10" height="7" fill="none" stroke="#f5821f" stroke-width="1.3"/><path d="M1 2.5 L6 6.5 L11 2.5" fill="none" stroke="#f5821f" stroke-width="1.3"/></svg>
      hello@verantaresearch.com
    </p>
    <p class="contact__line">
      <svg viewBox="0 0 12 12"><circle cx="6" cy="6" r="5" fill="none" stroke="#f5821f" stroke-width="1.2"/><ellipse cx="6" cy="6" rx="2.2" ry="5" fill="none" stroke="#f5821f" stroke-width="1"/><path d="M1 6 H11" stroke="#f5821f" stroke-width="1"/></svg>
      www.verantaresearch.com
    </p>
  </div>
  <svg class="band" viewBox="0 0 560 24" preserveAspectRatio="none" aria-hidden="true">
    <polygon points="0,14 400,14 380,24 0,24" fill="#f5821f"/>
    <polygon points="400,14 412,0 560,0 560,24 380,24" fill="#6b7a8b"/>
  </svg>
</section>

</body>
</html>
```